Recycling Right

We are creating a campaign to encourage (read motivate) people to recycle all their waste items correctly. A pictorial graphic that encourages recycling and diversion from landfill. A catchy graphic that can will go on all marketing. Could be serious or playful. Should have elements of recycling at its core. Could be a Recycling Character or Hero.
We want to have multifamily and commercial account to put the correct items in the blue recycle bins. We currently have a mixed recycling bin and will not be separating recyclables glass, plastic , paper at the bin

Target Market(s)

Residents primarily with some material going to businesses as well. all ages.

Colors

Designer to choose colors to be used in the design.

Requirements
Must have
• colorful, eye catching, be able to blow up to large billboard size or small letterhead size.
Nice to have
• bright colors,

```html
<!DOCTYPE html>
<html lang="en">
<head>
<meta charset="utf-8">
<title>Recycling Right</title>
<link rel="stylesheet" href="https://fonts.googleapis.com/css2?family=Montserrat:wght@400&family=Roboto:wght@900&display=swap">
<style>
  :root {
    --stage: #e6e8eb;
    --paper: #ffffff;
    --paper-shade: #f2f3f3;
    --leaf-light: #b9dcc0;
    --leaf-mid: #6cc07a;
    --leaf-deep: #2fae4a;
    --forest: #0d6136;
    --forest-fold: #0a4a29;
    --ribbon: #157a44;
    --arrow: #14934a;
    --ink: #1c1c1c;
  }
  html, body {
    margin: 0;
    width: 1200px;
    height: 1200px;
    overflow: hidden;
    background: var(--stage);
  }
  .flyer {
    position: absolute;
    left: 195px;
    top: 60px;
    width: 810px;
    height: 1080px;
    display: block;
  }
  .banner-title {
    font-family: "Roboto", Arial, sans-serif;
    font-weight: 900;
    font-size: 30px;
    letter-spacing: 2px;
    fill: var(--paper);
  }
  .contact-text {
    font-family: "Montserrat", Arial, sans-serif;
    font-weight: 400;
    font-size: 17px;
    fill: var(--ink);
  }
</style>
</head>
<body>
<svg class="flyer" viewBox="163 22 675 900" xmlns="http://www.w3.org/2000/svg">
  <defs>
    <linearGradient id="hillside" x1="0" y1="0" x2="0" y2="1">
      <stop offset="0" stop-color="var(--leaf-light)"/>
      <stop offset="0.55" stop-color="var(--leaf-mid)"/>
      <stop offset="1" stop-color="var(--leaf-deep)"/>
    </linearGradient>
    <linearGradient id="paper-fill" x1="0" y1="0" x2="0" y2="1">
      <stop offset="0" stop-color="var(--paper)"/>
      <stop offset="1" stop-color="var(--paper-shade)"/>
    </linearGradient>
    <marker id="arrowhead" viewBox="0 0 10 10" refX="6" refY="5" markerWidth="4" markerHeight="4" orient="auto">
      <path d="M0 0 L10 5 L0 10 Z" fill="var(--arrow)"/>
    </marker>
  </defs>

  <!-- header illustration area -->
  <rect class="hero-scene" x="163" y="22" width="675" height="400" fill="url(#hillside)"
        role="img" aria-label="Illustration of a green hill planted with trees, with families, birds and flowers under falling light specks"/>

  <!-- white body with wavy top edge -->
  <path class="body-panel" d="M163 412 C230 396 300 386 380 392 C450 398 500 374 560 380 C650 390 720 372 838 396 L838 922 L163 922 Z" fill="url(#paper-fill)"/>

  <!-- title ribbon -->
  <g class="title-ribbon">
    <path d="M352 463 L412 463 L412 520 L352 520 L368 491 Z" fill="var(--ribbon)"/>
    <path d="M648 463 L588 463 L588 520 L648 520 L632 491 Z" fill="var(--ribbon)"/>
    <path d="M403 520 L412 520 L412 528 Z" fill="var(--forest-fold)"/>
    <path d="M597 520 L588 520 L588 528 Z" fill="var(--forest-fold)"/>
    <rect x="403" y="440" width="194" height="80" fill="var(--forest)"/>
    <rect x="407" y="444" width="186" height="72" fill="none" stroke="var(--paper)" stroke-width="1.5"/>
    <text class="banner-title" x="500" y="472" text-anchor="middle">RECYCLING</text>
    <text class="banner-title" x="500" y="506" text-anchor="middle">RIGHT</text>
  </g>

  <!-- cycle arrows -->
  <g class="cycle-arrows" fill="none" stroke="var(--arrow)" stroke-width="4" marker-end="url(#arrowhead)">
    <polyline points="345,663 345,577 460,577"/>
    <polyline points="540,577 665,577 665,655"/>
    <polyline points="665,755 665,822 588,822"/>
    <polyline points="443,822 345,822 345,762"/>
  </g>

  <!-- recycling bin icon -->
  <g class="icon-bin">
    <path d="M466 535 L541 535 L531 615 L476 615 Z" fill="var(--forest)"/>
    <g fill="var(--paper)" transform="translate(503 574)">
      <path d="M-4 -15 L6 -15 L12 -5 L16 -7 L12 4 L2 1 L6 -1 L2 -8 L-4 2 L-9 -1 Z"/>
      <path d="M-4 -15 L6 -15 L12 -5 L16 -7 L12 4 L2 1 L6 -1 L2 -8 L-4 2 L-9 -1 Z" transform="rotate(120)"/>
      <path d="M-4 -15 L6 -15 L12 -5 L16 -7 L12 4 L2 1 L6 -1 L2 -8 L-4 2 L-9 -1 Z" transform="rotate(240)"/>
    </g>
  </g>

  <!-- collection truck icon -->
  <g class="icon-truck" fill="var(--forest)">
    <path d="M585 700 C592 684 604 678 620 678 L640 678 L640 728 L592 728 C587 728 585 724 585 720 Z"/>
    <rect x="643" y="682" width="62" height="46"/>
    <path d="M705 698 L716 698 L723 712 L723 728 L705 728 Z"/>
    <path d="M598 690 L628 686" stroke="var(--paper)" stroke-width="3"/>
    <circle cx="612" cy="733" r="8"/><circle cx="612" cy="733" r="3" fill="var(--paper)"/>
    <circle cx="700" cy="733" r="8"/><circle cx="700" cy="733" r="3" fill="var(--paper)"/>
  </g>

  <!-- sorting worker icon -->
  <g class="icon-sorting" fill="var(--forest)">
    <circle cx="534" cy="761" r="13"/>
    <path d="M513 806 L513 790 C513 780 520 776 534 776 C548 776 555 780 555 790 L555 806 Z"/>
    <rect x="479" y="788" width="14" height="16"/>
    <rect x="496" y="792" width="12" height="12"/>
    <rect x="470" y="808" width="90" height="5"/>
    <circle cx="485" cy="824" r="10"/><circle cx="485" cy="824" r="4" fill="var(--paper)"/>
    <circle cx="512" cy="824" r="10"/><circle cx="512" cy="824" r="4" fill="var(--paper)"/>
    <circle cx="539" cy="824" r="10"/><circle cx="539" cy="824" r="4" fill="var(--paper)"/>
    <rect x="470" y="834" width="90" height="5"/>
  </g>

  <!-- person using bin icon -->
  <g class="icon-disposal" fill="var(--forest)">
    <circle cx="313" cy="684" r="8"/>
    <path d="M302 696 L324 696 L338 712 L334 716 L324 706 L324 748 L316 748 L316 724 L310 724 L310 748 L302 748 Z"/>
    <path d="M344 714 L372 714 L368 748 L348 748 Z"/>
    <rect x="342" y="709" width="32" height="4"/>
    <rect x="350" y="720" width="16" height="22" fill="var(--paper)"/>
  </g>

  <!-- contact footer -->
  <g class="contact-footer">
    <line x1="192" y1="870" x2="808" y2="870" stroke="var(--forest)" stroke-width="1.5"/>
    <text class="contact-text" x="198" y="901">0123.456.789</text>
    <rect x="347" y="889" width="12" height="12" rx="2" fill="var(--forest)"/>
    <text class="contact-text" x="405" y="901">name@website.com</text>
    <rect x="605" y="889" width="12" height="12" rx="2" fill="var(--forest)"/>
    <text class="contact-text" x="643" y="901">yourwebsiite.com</text>
  </g>
</svg>
</body>
</html>
```